Crypto Exchange Comparison Platform

Let’s design a page that lets users compare hundreds of cryptocurrency exchanges. It will help users compare more info than anywhere else so you can find the best crypto exchange for your needs. The goal is to transform complex data into a clean, visually engaging experience.

Key Features to Design:
- Interactive comparison table with ~ 30 columns
- Filters and dropdown menus for easier usability
- Summary boxes for quick-view statistics
- Visual charts and graphs for key metrics
- Web, mobile, and tablet responsive design

Design Goals:
- Clean, modern aesthetic that makes complex data easily digestible
- Interactive elements (eg. Bar and Spider charts) for user engagement
- "Screenshot-friendly" sections for social media and sharing
- Data visualization focus (charts, graphs, metrics)
- Extremely easy to use on mobile
- Designs that use the color green
- A brand that communicates research and trusted information

Deliverables:
- High-fidelity mockup for desktop, tablet, and mobile versions
- Interactive prototype (Figma preferred)
- Style guide (typography, colors, components)

Note: The goal is to create an intuitive, visually engaging tool that helps users compare cryptocurrency exchanges efficiently while maintaining a clean, professional appearance that works well for social media sharing and content creation.
Updates

Low design quality

Industry/Entity Type

FinTech, Crypto, Finance

Number of Pages Required

1 page

Font styles to use
Other font styles liked:
• Inter or something good for a finance/data related website site

Colors
00AB8E
00BBA5
67D7C9
C6EFE9
E9F9F6

Requirements
Must have
• Please refer to the sketch I uploaded

```html
<!DOCTYPE html>
<html lang="en">
<head>
<meta charset="utf-8">
<title>Crypto Exchange – Compare Crypto Exchanges</title>
<link href="https://fonts.googleapis.com/css2?family=Inter:wght@400;500;600;700&family=Montserrat:wght@500;600;700&display=swap" rel="stylesheet">
<style>
:root{
  --green:#00AB8E;
  --green-2:#00BBA5;
  --green-3:#67D7C9;
  --green-4:#C6EFE9;
  --green-5:#E9F9F6;
  --ink:#1d2b2a;
  --muted:#8a9996;
  --line:#e4efed;
  --white:#fff;
}
*{box-sizing:border-box;margin:0;padding:0}
html,body{width:1200px;height:4598px;overflow:hidden}
body{position:relative;font-family:Inter,sans-serif;color:var(--ink);background:#fff}
.abs{position:absolute}
h1,h2,h3,.brand{font-family:Montserrat,sans-serif}

/* hero */
.hero{left:0;top:0;width:1200px;height:562px;background:linear-gradient(160deg,#1fc7b0 0%,var(--green-2) 45%,#12a58f 100%)}
.nav{left:105px;top:18px;width:990px;height:40px;display:flex;align-items:center;color:#fff}
.brand{font-size:25px;font-weight:600;margin-right:46px}
.nav a{color:#fff;text-decoration:none;font-size:12.5px;font-weight:500;margin-right:33px}
.nav .cta{margin-left:auto;margin-right:0;border:1.5px solid #fff;border-radius:20px;padding:9px 28px}
.hero h1{left:0;top:158px;width:1200px;text-align:center;color:#fff;font-size:52px;font-weight:500;letter-spacing:.5px}
.hero h1 span{background:var(--green-3);color:#fff;font-weight:600;padding:0 18px;margin-left:10px}
.pill{top:264px;width:285px;height:59px;background:#fff;border-radius:30px;display:flex;align-items:center;justify-content:center;gap:12px;font-size:17px;font-weight:500}
.pill svg{width:20px;height:20px}
.section-title{font-size:31px;font-weight:600}
.picks-title{left:102px;top:432px;color:#fff}
.picks{left:102px;top:491px;width:1010px;height:145px;background:#fff;border:1px solid var(--line);box-shadow:0 6px 20px rgba(0,80,70,.08);display:flex}
.pick{flex:1;padding:30px 34px;display:flex;gap:20px;border-right:1px solid var(--line)}
.pick:last-child{border-right:none}
.pick .dot{width:54px;height:54px;border-radius:50%;flex:none}
.pick h3{font-size:21px;font-weight:600;margin-top:4px}
.pick p{font-size:14px;color:#a2aead;margin:8px 0 6px}
.pick .url{font-size:14px;display:flex;align-items:center;gap:6px}

/* tabs */
.tab{top:732px;height:43px;border:1px solid var(--green-4);display:flex;align-items:center;justify-content:center;gap:8px;font-size:14px;font-weight:600;color:var(--green)}
.tab.on{background:var(--green);color:#fff;border-color:var(--green)}
.compare-btn{left:970px;top:732px;width:146px;height:43px;border:1px solid var(--green-4);display:flex;align-items:center;justify-content:center;gap:8px;font-size:15px;font-weight:600}

/* table */
.table{left:95px;top:814px;width:1030px;height:1020px;border:1px solid var(--line);font-size:11px}
.row{display:grid;grid-template-columns:70px 108px 102px 92px 145px 140px 152px 88px 133px;height:37px;align-items:center}
.row>div{text-align:center}
.row>div:nth-child(2){text-align:left}
.row.head{height:56px;background:var(--green-5);font-size:12px;font-weight:500}
.row:nth-child(odd):not(.head){background:#f3fbf9}
.ex{display:flex;align-items:center;gap:6px;font-size:9.5px}
.ex i{width:14px;height:14px;border-radius:50%;display:inline-block;background:var(--c)}
.pager{left:500px;top:1856px;display:flex;gap:18px;align-items:center;font-size:12px}
.pager span{width:28px;height:26px;display:flex;align-items:center;justify-content:center}
.pager .cur{background:var(--green-5);border-radius:3px}
.rows-sel{left:958px;top:1856px;display:flex;align-items:center;gap:12px;font-size:11px;color:var(--muted)}
.rows-sel b{width:88px;height:28px;border:1px solid var(--line);display:flex;align-items:center;justify-content:space-between;padding:0 12px;font-weight:400;color:var(--ink)}

/* charts */
.panel{top:1954px;height:375px;border:2px solid var(--green-4);background:#fff}
.panel h3{position:absolute;left:22px;top:25px;font-size:23px;font-weight:500;display:flex;gap:12px;align-items:center}
.stat{top:2352px;height:173px;border:2px solid var(--green-4);padding:18px 24px;overflow:hidden}
.stat h4{font-size:17px;font-weight:500}
.stat .big{font-family:Montserrat,sans-serif;font-size:42px;font-weight:700;color:var(--green);margin-top:4px}
.stat small{display:block;font-size:10px;margin-top:6px}
.stat.fill{background:var(--green-2);border-color:var(--green-2);color:#fff}
.stat.fill .big{color:#fff}
.stat.soft{background:var(--green-5);border-color:var(--green-5)}
.stat svg{position:absolute;left:0;bottom:0}

/* compare */
.compare-bg{left:0;top:2593px;width:1200px;height:952px;background:var(--green-5)}
.compare-title{left:127px;top:2660px;font-size:38px}
.sel{top:2673px;width:176px;height:45px;background:#fff;border:1px solid var(--green-4);display:flex;align-items:center;padding:0 18px;gap:8px;font-size:15px}
.sel svg:last-child{margin-left:auto}
.card{background:#fff;box-shadow:0 4px 18px rgba(0,80,70,.06)}
.scores{position:absolute;left:35px;top:294px;width:273px;font-size:12px}
.scores div{display:grid;grid-template-columns:115px 75px 83px;height:44px;align-items:center;border-bottom:1px solid var(--line)}
.scores div:first-child{background:var(--green-4);height:38px;border:none}
.scores span:first-child{color:var(--green);padding-left:12px}
.scores span{text-align:center}
.scores span:first-child{text-align:left}
.feat-head{position:absolute;left:42px;top:36px;display:flex;gap:12px;align-items:center;font-weight:600;font-size:16px;letter-spacing:.5px}
.feat-rows{position:absolute;left:32px;top:78px;width:560px;font-size:16px}
.feat-rows div{display:grid;grid-template-columns:225px 225px 110px;height:48px;align-items:center;padding-left:18px}
.feat-rows div:nth-child(odd){background:var(--green-5)}
.acc{position:absolute;left:42px;width:540px;height:72px;border-bottom:1px solid var(--green-4);display:flex;align-items:center;gap:14px;font-weight:600;font-size:16px;letter-spacing:.5px}
.acc svg:last-child{margin-left:auto}

/* faq */
.faq-title{left:0;top:3630px;width:1200px;text-align:center;font-size:33px;font-weight:700}
.faq-title span{font-weight:400}
.faq{left:177px;width:868px;height:63px;border:2px solid var(--green-4);display:flex;align-items:center;padding:0 38px;font-size:17px;font-weight:600;justify-content:space-between}
.faq.open{height:157px;display:block;padding-top:22px}
.faq.open .q{display:flex;justify-content:space-between}
.faq.open p{font-size:12.5px;font-weight:400;color:#5f6d6a;margin-top:20px;line-height:1.7;padding-right:40px}

/* footer */
.footer{left:0;top:4267px;width:1200px;height:331px;background:linear-gradient(135deg,#11b49c,var(--green) 60%,#079a82);color:#fff}
.footer .brand{position:absolute;left:120px;top:86px;font-size:25px;font-weight:500}
.footer .about{position:absolute;left:120px;top:140px;width:270px;font-size:12px;line-height:1.9}
.footer .copy{position:absolute;left:120px;top:224px;font-size:12px}
.fcol{position:absolute;top:74px}
.fcol h4{font-family:Montserrat,sans-serif;font-size:19px;font-weight:600;border-left:3px solid #fff;padding-left:12px;margin-bottom:20px}
.fcol a{display:block;color:#fff;text-decoration:none;font-size:12.5px;line-height:23px;padding-left:18px}
.social{display:flex;gap:24px;padding-left:18px}
.social i{width:24px;height:24px;border-radius:50%;background:#fff;display:block}
</style>
</head>
<body>

<!-- hero -->
<section class="abs hero">
  <nav class="abs nav">
    <span class="brand">Crypto Exchange</span>
    <a href="#">Crypto Currencies</a><a href="#">Exchanges</a><a href="#">Learn</a><a href="#">How it Works</a><a href="#">API</a><a href="#">Resources</a>
    <a href="#" class="cta">Get Started</a>
  </nav>
  <h1 class="abs">Compare Crypto <span>Exchange</span></h1>
  <div class="abs pill" style="left:170px"><svg viewBox="0 0 20 20"><path d="M2 2v16h16" stroke="#1d2b2a" stroke-width="2" fill="none"/><path d="M6 14V9M10 14V6M14 14V10" stroke="#00AB8E" stroke-width="2.4"/></svg>Platform Tracked: 125</div>
  <div class="abs pill" style="left:470px"><svg viewBox="0 0 20 20"><rect x="2" y="4" width="16" height="14" rx="2" stroke="#00AB8E" stroke-width="2" fill="none"/><path d="M2 8h16M6 2v4M14 2v4" stroke="#00AB8E" stroke-width="2"/></svg>Updated: Feb 16, 2025</div>
  <div class="abs pill" style="left:768px"><svg viewBox="0 0 22 20"><circle cx="8" cy="6" r="4" fill="#00AB8E"/><path d="M1 18c0-4 3-7 7-7s7 3 7 7z" fill="#00AB8E"/><circle cx="17" cy="14" r="3" stroke="#00AB8E" stroke-width="2" fill="none"/></svg>How We Test</div>
  <h2 class="abs section-title picks-title">Top Picks</h2>
</section>
<div class="abs picks">
  <div class="pick"><span class="dot" style="background:var(--green)"></span><div><h3>Pionar</h3><p>Lorem ipsum dolor sit</p><div class="url"><svg width="14" height="14" viewBox="0 0 14 14"><circle cx="7" cy="7" r="6" stroke="#00AB8E" fill="none" stroke-width="1.4"/><path d="M1 7h12M7 1c3 3 3 9 0 12M7 1c-3 3-3 9 0 12" stroke="#00AB8E" fill="none"/></svg>www.pionar-app.com</div></div></div>
  <div class="pick"><span class="dot" style="background:#0e8f7a"></span><div><h3>Extener Up</h3><p>Lorem ipsum dolor sit</p><div class="url"><svg width="14" height="14" viewBox="0 0 14 14"><circle cx="7" cy="7" r="6" stroke="#00AB8E" fill="none" stroke-width="1.4"/><path d="M1 7h12M7 1c3 3 3 9 0 12M7 1c-3 3-3 9 0 12" stroke="#00AB8E" fill="none"/></svg>www.pionar-app.com</div></div></div>
  <div class="pick"><span class="dot" style="background:#f0a21d"></span><div><h3>Tidemark</h3><p>Lorem ipsum dolor sit</p><div class="url"><svg width="14" height="14" viewBox="0 0 14 14"><circle cx="7" cy="7" r="6" stroke="#00AB8E" fill="none" stroke-width="1.4"/><path d="M1 7h12M7 1c3 3 3 9 0 12M7 1c-3 3-3 9 0 12" stroke="#00AB8E" fill="none"/></svg>www.pionar-app.com</div></div></div>
</div>

<!-- tabs -->
<div class="abs tab on" style="left:95px;width:146px"><svg width="16" height="16"><circle cx="8" cy="8" r="7" fill="#fff"/></svg>Fees</div>
<div class="abs tab" style="left:248px;width:147px"><svg width="16" height="14"><rect x="1" y="8" width="4" height="5" fill="#00AB8E"/><rect x="6" y="3" width="4" height="10" fill="#00AB8E"/><rect x="11" y="6" width="4" height="7" fill="#00AB8E"/></svg>Features</div>
<div class="abs tab" style="left:400px;width:147px"><svg width="12" height="14"><path d="M6 1l5 2v4c0 3-2 5-5 6-3-1-5-3-5-6V3z" stroke="#00AB8E" fill="none" stroke-width="1.4"/></svg>Security</div>
<div class="abs compare-btn"><svg width="16" height="16"><path d="M2 14L14 2M9 2h5v5M2 9v5h5" stroke="#00AB8E" stroke-width="1.6" fill="none"/></svg>Compare<svg width="14" height="10"><path d="M2 2l5 5 5-5" stroke="#00AB8E" stroke-width="1.8" fill="none"/></svg></div>

<!-- table -->
<div class="abs table">
  <div class="row head"><div>#</div><div>Exchange</div><div>Maker Fee</div><div>Taker Fee</div><div>Futures Maker Fee</div><div>Futures Taker Fee</div><div>Trading Fee Discount</div><div>Discount</div><div>Visit</div></div>
  <div class="row"><div>1</div><div class="ex"><i style="--c:#f3ba2f"></i>Vantor</div><div>$12.50</div><div>$8.50</div><div>$6.50</div><div>$4.80</div><div>$2.50</div><div>5%</div><div>www.exq.app</div></div>
  <div class="row"><div>2</div><div class="ex"><i style="--c:#1652f0"></i>Coinhaven</div><div>$12.50</div><div>$8.50</div><div>$6.50</div><div>$4.80</div><div>$2.50</div><div>5%</div><div>www.exq.app</div></div>
  <div class="row"><div>3</div><div class="ex"><i style="--c:#111"></i>Orbix</div><div>$12.50</div><div>$8.50</div><div>$6.50</div><div>$4.80</div><div>$2.50</div><div>5%</div><div>www.exq.app</div></div>
  <div class="row"><div>4</div><div class="ex"><i style="--c:#102a4c"></i>Cryptora</div><div>$12.50</div><div>$8.50</div><div>$6.50</div><div>$4.80</div><div>$2.50</div><div>5%</div><div>www.exq.app</div></div>
  <div class="row"><div>5</div><div class="ex"><i style="--c:#5741d9"></i>Tidemark</div><div>$12.50</div><div>$8.50</div><div>$6.50</div><div>$4.80</div><div>$2.50</div><div>5%</div><div>www.exq.app</div></div>
  <div class="row"><div>6</div><div class="ex"><i style="--c:#2354e6"></i>Gatewell</div><div>$12.50</div><div>$8.50</div><div>$6.50</div><div>$4.80</div><div>$2.50</div><div>5%</div><div>www.exq.app</div></div>
  <div class="row"><div>7</div><div class="ex"><i style="--c:#00c0d8"></i>Bitreach Exchange</div><div>$12.50</div><div>$8.50</div><div>$6.50</div><div>$4.80</div><div>$2.50</div><div>5%</div><div>www.exq.app</div></div>
  <div class="row"><div>8</div><div class="ex"><i style="--c:#222"></i>Bitmoor</div><div>$12.50</div><div>$8.50</div><div>$6.50</div><div>$4.80</div><div>$2.50</div><div>5%</div><div>www.exq.app</div></div>
  <div class="row"><div>9</div><div class="ex"><i style="--c:#f3ba2f"></i>Vantor</div><div>$12.50</div><div>$8.50</div><div>$6.50</div><div>$4.80</div><div>$2.50</div><div>5%</div><div>www.exq.app</div></div>
  <div class="row"><div>10</div><div class="ex"><i style="--c:#1652f0"></i>Coinhaven</div><div>$12.50</div><div>$8.50</div><div>$6.50</div><div>$4.80</div><div>$2.50</div><div>5%</div><div>www.exq.app</div></div>
  <div class="row"><div>11</div><div class="ex"><i style="--c:#111"></i>Orbix</div><div>$12.50</div><div>$8.50</div><div>$6.50</div><div>$4.80</div><div>$2.50</div><div>5%</div><div>www.exq.app</div></div>
  <div class="row"><div>12</div><div class="ex"><i style="--c:#102a4c"></i>Cryptora</div><div>$12.50</div><div>$8.50</div><div>$6.50</div><div>$4.80</div><div>$2.50</div><div>5%</div><div>www.exq.app</div></div>
  <div class="row"><div>13</div><div class="ex"><i style="--c:#5741d9"></i>Tidemark</div><div>$12.50</div><div>$8.50</div><div>$6.50</div><div>$4.80</div><div>$2.50</div><div>5%</div><div>www.exq.app</div></div>
  <div class="row"><div>14</div><div class="ex"><i style="--c:#2354e6"></i>Gatewell</div><div>$12.50</div><div>$8.50</div><div>$6.50</div><div>$4.80</div><div>$2.50</div><div>5%</div><div>www.exq.app</div></div>
  <div class="row"><div>15</div><div class="ex"><i style="--c:#00c0d8"></i>Bitreach Exchange</div><div>$12.50</div><div>$8.50</div><div>$6.50</div><div>$4.80</div><div>$2.50</div><div>5%</div><div>www.exq.app</div></div>
  <div class="row"><div>16</div><div class="ex"><i style="--c:#222"></i>Bitmoor</div><div>$12.50</div><div>$8.50</div><div>$6.50</div><div>$4.80</div><div>$2.50</div><div>5%</div><div>www.exq.app</div></div>
  <div class="row"><div>17</div><div class="ex"><i style="--c:#f3ba2f"></i>Vantor</div><div>$12.50</div><div>$8.50</div><div>$6.50</div><div>$4.80</div><div>$2.50</div><div>5%</div><div>www.exq.app</div></div>
  <div class="row"><div>18</div><div class="ex"><i style="--c:#1652f0"></i>Coinhaven</div><div>$12.50</div><div>$8.50</div><div>$6.50</div><div>$4.80</div><div>$2.50</div><div>5%</div><div>www.exq.app</div></div>
  <div class="row"><div>19</div><div class="ex"><i style="--c:#111"></i>Orbix</div><div>$12.50</div><div>$8.50</div><div>$6.50</div><div>$4.80</div><div>$2.50</div><div>5%</div><div>www.exq.app</div></div>
  <div class="row"><div>20</div><div class="ex"><i style="--c:#102a4c"></i>Cryptora</div><div>$12.50</div><div>$8.50</div><div>$6.50</div><div>$4.80</div><div>$2.50</div><div>5%</div><div>www.exq.app</div></div>
  <div class="row"><div>21</div><div class="ex"><i style="--c:#5741d9"></i>Tidemark</div><div>$12.50</div><div>$8.50</div><div>$6.50</div><div>$4.80</div><div>$2.50</div><div>5%</div><div>www.exq.app</div></div>
  <div class="row"><div>22</div><div class="ex"><i style="--c:#2354e6"></i>Gatewell</div><div>$12.50</div><div>$8.50</div><div>$6.50</div><div>$4.80</div><div>$2.50</div><div>5%</div><div>www.exq.app</div></div>
  <div class="row"><div>23</div><div class="ex"><i style="--c:#00c0d8"></i>Bitreach Exchange</div><div>$12.50</div><div>$8.50</div><div>$6.50</div><div>$4.80</div><div>$2.50</div><div>5%</div><div>www.exq.app</div></div>
  <div class="row"><div>24</div><div class="ex"><i style="--c:#222"></i>Bitmoor</div><div>$12.50</div><div>$8.50</div><div>$6.50</div><div>$4.80</div><div>$2.50</div><div>5%</div><div>www.exq.app</div></div>
  <div class="row"><div>25</div><div class="ex"><i style="--c:#102a4c"></i>Cryptora</div><div>$12.50</div><div>$8.50</div><div>$6.50</div><div>$4.80</div><div>$2.50</div><div>5%</div><div>www.exq.app</div></div>
</div>
<div class="abs pager"><span>‹</span><span class="cur">1</span><span>2</span><span>3</span><span>4</span><span>5</span><span>›</span></div>
<div class="abs rows-sel">Show rows <b>25 <svg width="12" height="8"><path d="M1 1l5 5 5-5" stroke="#1d2b2a" stroke-width="1.5" fill="none"/></svg></b></div>

<!-- charts -->
<div class="abs panel" style="left:93px;width:509px">
  <h3><svg width="16" height="10"><path d="M1 1l7 7 7-7" stroke="#00AB8E" stroke-width="2" fill="none"/></svg>Maker Fees</h3>
  <svg class="abs" style="left:20px;top:80px" width="470" height="280" viewBox="0 0 470 280" font-family="Inter" font-size="11" fill="#555">
    <g stroke="#e6eceb"><path d="M40 10H450M40 58H450M40 106H450M40 154H450M40 202H450M40 250H450"/></g>
    <text x="14" y="14">30</text><text x="14" y="62">25</text><text x="14" y="110">20</text><text x="14" y="158">15</text><text x="14" y="206">10</text><text x="20" y="254">5</text><text x="20" y="292" dy="-34">0</text>
    <g fill="#00AB8E">
      <rect x="60" y="154" width="17" height="96"/><rect x="96" y="81" width="17" height="169"/><rect x="150" y="101" width="17" height="149"/><rect x="204" y="173" width="17" height="77"/><rect x="246" y="14" width="17" height="236"/><rect x="272" y="138" width="17" height="112"/><rect x="326" y="105" width="17" height="145"/><rect x="360" y="120" width="17" height="130"/><rect x="424" y="32" width="17" height="218"/>
    </g>
    <g fill="#9ee3d8">
      <rect x="42" y="198" width="17" height="52"/><rect x="124" y="178" width="17" height="72"/><rect x="222" y="180" width="17" height="70"/><rect x="306" y="198" width="17" height="52"/><rect x="398" y="198" width="17" height="52"/>
    </g>
    <g fill="#67D7C9"><rect x="178" y="198" width="17" height="52"/></g>
    <g font-size="9" fill="#00AB8E"><text x="40" y="272">2016</text><text x="90" y="272">2017</text><text x="140" y="272">2018</text><text x="190" y="272">2019</text><text x="240" y="272">2020</text><text x="286" y="272">2021</text><text x="336" y="272">2022</text><text x="380" y="272">2023</text><text x="424" y="272">2024</text></g>
  </svg>
</div>
<div class="abs panel" style="left:618px;width:511px">
  <h3><svg width="16" height="10"><path d="M1 1l7 7 7-7" stroke="#00AB8E" stroke-width="2" fill="none"/></svg>Trading Volume</h3>
  <svg class="abs" style="left:0;top:0" width="507" height="371" viewBox="0 0 507 371">
    <defs><linearGradient id="vol" x1="0" y1="0" x2="0" y2="1"><stop offset="0" stop-color="#67D7C9" stop-opacity=".45"/><stop offset="1" stop-color="#E9F9F6" stop-opacity=".2"/></linearGradient></defs>
    <path d="M0 272L40 225L68 258L100 190L148 192L170 232L198 200L226 138L258 168L295 193L320 148L365 85L395 130L420 145L448 170L475 150L507 170V371H0Z" fill="url(#vol)"/>
    <polyline points="0,272 40,225 68,258 100,190 148,192 170,232 198,200 226,138 258,168 295,193 320,148 365,85 395,130 420,145 448,170 475,150 507,170" fill="none" stroke="#3cc7b2" stroke-width="2"/>
    <g fill="#fff" stroke="#3cc7b2" stroke-width="2"><circle cx="40" cy="225" r="5"/><circle cx="148" cy="192" r="5"/><circle cx="226" cy="138" r="5"/><circle cx="295" cy="193" r="5"/><circle cx="365" cy="85" r="5"/><circle cx="468" cy="155" r="5"/></g>
  </svg>
</div>

<div class="abs stat" style="left:95px;width:248px"><h4>Exchange Tracked</h4><div class="big">125</div>
  <svg width="244" height="70"><path d="M18 55C40 40 50 25 70 40S100 20 120 35S150 28 165 40S190 25 210 40V70H18Z" fill="#E9F9F6"/><path d="M18 55C40 40 50 25 70 40S100 20 120 35S150 28 165 40S190 25 210 40" stroke="#67D7C9" stroke-width="1.8" fill="none"/></svg></div>
<div class="abs stat" style="left:359px;width:245px"><h4>Average Trading Fee</h4><div class="big">0.15%</div>
  <svg width="241" height="90"><path d="M40 80C60 50 70 60 90 40S120 20 140 25S170 0 200 10S220 20 225 15" stroke="#67D7C9" stroke-width="1.5" fill="none"/><path d="M40 70C70 60 90 45 110 50S150 30 180 25" stroke="#C6EFE9" stroke-width="1.5" fill="none"/></svg></div>
<div class="abs stat fill" style="left:618px;width:246px"><h4>Total Users</h4><small>Lorem ipsum dolor sit amet, consectetur</small><div class="big">892M</div></div>
<div class="abs stat soft" style="left:879px;width:246px"><h4>Web Visitor (30D)</h4><small>Lorem ipsum dolor sit amet, consectetur</small><div class="big">12.2B</div></div>

<!-- compare -->
<div class="abs compare-bg"></div>
<svg class="abs" style="left:0;top:2680px" width="110" height="10"><path d="M0 5H96" stroke="#00AB8E" stroke-width="1.5"/><circle cx="100" cy="5" r="4" fill="#00AB8E"/></svg>
<h2 class="abs section-title compare-title">Compare</h2>
<div class="abs sel" style="left:734px"><svg width="16" height="16"><path d="M8 1l7 7-7 7-7-7z" stroke="#00AB8E" fill="none" stroke-width="1.5"/></svg>Vantor<svg width="14" height="9"><path d="M1 1l6 6 6-6" stroke="#00AB8E" stroke-width="1.8" fill="none"/></svg></div>
<div class="abs sel" style="left:923px"><svg width="16" height="16"><circle cx="8" cy="8" r="7" stroke="#00AB8E" fill="none" stroke-width="1.5"/></svg>Coinhaven<svg width="14" height="9"><path d="M1 1l6 6 6-6" stroke="#00AB8E" stroke-width="1.8" fill="none"/></svg></div>

<div class="abs card" style="left:120px;top:2756px;width:334px;height:682px">
  <svg class="abs" style="left:0;top:20px" width="334" height="240" viewBox="0 0 334 240" font-family="Inter" font-size="12" font-weight="500" fill="#00AB8E">
    <polygon points="166,32 243,88 214,178 118,178 89,88" fill="none" stroke="#67D7C9" stroke-width="2"/>
    <polygon points="166,44 232,92 206,170 126,170 100,92" fill="none" stroke="#C6EFE9" stroke-width="1.5"/>
    <polygon points="166,56 222,100 198,160 134,160 116,96" fill="#67D7C9" opacity=".55"/>
    <polygon points="166,70 210,104 190,150 140,152 126,100" fill="#00AB8E" opacity=".35"/>
    <g fill="#00AB8E"><circle cx="166" cy="32" r="3"/><circle cx="243" cy="88" r="3"/><circle cx="214" cy="178" r="3"/><circle cx="118" cy="178" r="3"/><circle cx="89" cy="88" r="3"/></g>
    <text x="150" y="20">Fees</text><text x="246" y="104">Features</text><text x="36" y="84">Security</text><text x="78" y="200">Deposits</text><text x="180" y="202">Withdrawals</text>
  </svg>
  <div class="scores">
    <div><span></span><span>Vantor</span><span>Coinhaven</span></div>
    <div><span>Fees</span><span>9/10</span><span>9/10</span></div>
    <div><span>Security</span><span>9/10</span><span>9/10</span></div>
    <div><span>Features</span><span>9/10</span><span>9/10</span></div>
    <div><span>Deposits</span><span>9/10</span><span>9/10</span></div>
    <div><span>Withdrawals</span><span>9/10</span><span>9/10</span></div>
  </div>
</div>

<div class="abs card" style="left:475px;top:2756px;width:622px;height:682px">
  <div class="feat-head"><svg width="20" height="18"><rect x="1" y="10" width="5" height="7" fill="#00AB8E"/><rect x="7.5" y="2" width="5" height="15" fill="#00AB8E"/><rect x="14" y="7" width="5" height="10" fill="#00AB8E"/></svg>FEATURES<svg style="position:absolute;left:494px" width="16" height="10"><path d="M1 9l7-7 7 7" stroke="#00AB8E" stroke-width="2" fill="none"/></svg></div>
  <div class="feat-rows">
    <div><span># of Coins</span><span>BAC</span><span>BAC</span></div>
    <div><span># of Futures</span><span>ABC</span><span>ABC</span></div>
    <div><span>Trading Bots</span><span>XYX</span><span>XYX</span></div>
    <div><span>Copy Trading</span><span>MIN</span><span>MIN</span></div>
    <div><span>24/7 Support</span><span>UBP</span><span>UBP</span></div>
  </div>
  <div class="acc" style="top:335px"><svg width="16" height="18"><path d="M8 1l7 3v5c0 4-3 7-7 8-4-1-7-4-7-8V4z" fill="#00AB8E"/></svg>SECURITY<svg width="16" height="10"><path d="M1 1l7 7 7-7" stroke="#00AB8E" stroke-width="2" fill="none"/></svg></div>
  <div class="acc" style="top:407px"><svg width="18" height="18"><circle cx="9" cy="9" r="8" fill="#00AB8E"/></svg>FEES<svg width="16" height="10"><path d="M1 1l7 7 7-7" stroke="#00AB8E" stroke-width="2" fill="none"/></svg></div>
  <div class="acc" style="top:480px"><svg width="18" height="18"><rect x="1" y="3" width="16" height="5" fill="#00AB8E"/><rect x="4" y="9" width="10" height="8" fill="#00AB8E"/></svg>DEPOSITS<svg width="16" height="10"><path d="M1 1l7 7 7-7" stroke="#00AB8E" stroke-width="2" fill="none"/></svg></div>
  <div class="acc" style="top:551px"><svg width="22" height="16"><rect x="1" y="2" width="20" height="12" rx="2" fill="#00AB8E"/><circle cx="11" cy="8" r="3" fill="#fff"/></svg>WITHDRAWALS<svg width="16" height="10"><path d="M1 1l7 7 7-7" stroke="#00AB8E" stroke-width="2" fill="none"/></svg></div>
</div>

<svg class="abs" style="left:618px;top:3504px" width="10" height="80"><path d="M5 0V72" stroke="#00AB8E" stroke-width="1.5"/><circle cx="5" cy="75" r="4" fill="#00AB8E"/></svg>

<!-- faq -->
<h2 class="abs faq-title">Frequently Asked <span>Questions</span></h2>
<div class="abs faq" style="top:3718px">What Are Crypto Exchanges?<svg width="16" height="10"><path d="M1 1l7 7 7-7" stroke="#00AB8E" stroke-width="2" fill="none"/></svg></div>
<div class="abs faq" style="top:3798px">How To Choose a Crypto Exchange?<svg width="16" height="10"><path d="M1 1l7 7 7-7" stroke="#00AB8E" stroke-width="2" fill="none"/></svg></div>
<div class="abs faq" style="top:3879px">How is this data tracked?<svg width="16" height="10"><path d="M1 1l7 7 7-7" stroke="#00AB8E" stroke-width="2" fill="none"/></svg></div>
<div class="abs faq" style="top:3959px">How often is this page updated?<svg width="16" height="10"><path d="M1 1l7 7 7-7" stroke="#00AB8E" stroke-width="2" fill="none"/></svg></div>
<div class="abs faq open" style="top:4039px">
  <div class="q">How to Crypto Exchanges?<svg width="16" height="10"><path d="M1 9l7-7 7 7" stroke="#00AB8E" stroke-width="2" fill="none"/></svg></div>
  <p>Lorem ipsum dolor sit amet, consectetur adipiscing elit, sed do eiusmod tempor incididunt ut labore et dolore magna aliqua. Quis ipsum suspendisse ultrices gravida. Risus commodo viverra maecenas accumsan lacus vel facilisis.</p>
</div>

<!-- footer -->
<footer class="abs footer">
  <div class="brand">Crypto Exchange</div>
  <p class="about">Lorem ipsum dolor sit amet, consectetur adipiscing elit, sed do eiusmod tempor incididunt ut labore</p>
  <p class="copy">© 2025 Crypto Exchange. All Rights Reserved</p>
  <div class="fcol" style="left:470px"><h4>Navigation</h4><a href="#">Crypto Currencies</a><a href="#">Exchanges</a><a href="#">Learn</a><a href="#">How it Works</a><a href="#">API</a><a href="#">Resources</a></div>
  <div class="fcol" style="left:684px"><h4>Resources</h4><a href="#">Terms &amp; Conditions</a><a href="#">FAQ</a><a href="#">Privacy Policy</a><a href="#">Blog</a><a href="#">Sitemap</a><a href="#">Contact Us</a></div>
  <div class="fcol" style="left:908px"><h4>Follow us</h4><div class="social"><i></i><i></i><i></i><i></i></div></div>
</footer>

</body>
</html>
```